New business card for my lawn and landscape business

Dorrin Yard and Building is a full-service lawn care, landscaping, and light construction company serving Paragould and the Northeast Arkansas region. The business is owned and operated by Marcus Toller, with a reputation for hands-on, detail-oriented service, dependable crews, and quality results for both residential and commercial clients. A well regarded business with great reviews.
Owner Marcus Toller
Dorrinyardandbuilding.example

Target Market(s)

Commercial, Middle, and upper class in north east Arkansas

Industry/Entity Type

Lawn maintenance and landscape

Contact Information for Business Card

Dorrin Yard And Building Professional lawn care, landscaping, and property improvement in Northeast Arkansas. • lawn maintenance •lawn treatments and weed control • exterior projects • Custom landscape design & installation • Sod, trees, rock & drainage solutions • Residential & commercial services Reliable. Detailed. Done right.

Requirements
Must have
• Business name, service area, list of some of our services, clean design that represents
Nice to have
• Unique. Different design element than just grass because its already in n the logo. Picture of a warm season (south) lawn or landscape. Pictures of the type of work we do

```html
<!DOCTYPE html>
<html lang="en">
<head>
<meta charset="utf-8">
<title>Dorrin Yard And Building – Business Card</title>
<link href="https://fonts.googleapis.com/css2?family=Poppins:ital,wght@0,400;0,600;1,400&display=swap" rel="stylesheet">
<style>
  :root {
    --backdrop: #e4e4e4;
    --card: #ffffff;
    --slate: #8c8c8c;
    --leaf: #76b043;
    --ink-light: #ffffff;
    --ink-dark: #7a7a7a;
  }
  * { box-sizing: border-box; margin: 0; padding: 0; }
  html, body {
    width: 1200px; height: 1200px; overflow: hidden;
    background: var(--backdrop);
    font-family: "Poppins", sans-serif;
  }
  .card {
    position: absolute; left: 169px; width: 864px; height: 505px;
    background: var(--card); overflow: hidden;
  }
  .card-front { top: 78px; }
  .card-back { top: 618px; }
  .front-shapes { position: absolute; inset: 0; }
  .tagline {
    position: absolute; left: 50px; top: 48px; width: 790px; height: 82px;
    display: flex; align-items: center;
    color: var(--ink-light); font-size: 20.5px; line-height: 1.35; letter-spacing: 0.2px;
  }
  .services {
    position: absolute; left: 50px; top: 168px; list-style: none;
    color: var(--ink-light); font-style: italic; font-size: 18.5px; letter-spacing: 0.3px;
  }
  .services li { height: 46px; line-height: 46px; }
  .services li::before { content: "• "; }
  .brand {
    position: absolute; display: flex; align-items: center; gap: 14px;
  }
  .brand-dot { border-radius: 50%; background: var(--slate); flex: none; }
  .brand-name {
    color: var(--leaf); font-weight: 600; line-height: 1.05; text-transform: uppercase;
  }
  .brand-front { left: 590px; top: 300px; width: 260px; }
  .brand-front .brand-dot { width: 34px; height: 34px; }
  .brand-front .brand-name { font-size: 24px; }
  .brand-back { left: 0; right: 0; top: 0; bottom: 0; justify-content: center; gap: 26px; }
  .brand-back .brand-dot { width: 70px; height: 70px; }
  .brand-back .brand-name { font-size: 50px; }
</style>
</head>
<body>
  <section class="card card-front">
    <svg class="front-shapes" width="864" height="505" viewBox="0 0 864 505" aria-hidden="true">
      <polygon points="0,0 594,0 491,505 0,505" fill="var(--slate)"/>
      <rect x="0" y="48" width="864" height="82" fill="var(--leaf)"/>
      <polygon points="568,204 583,204 514,505 499,505" fill="var(--leaf)"/>
    </svg>
    <p class="tagline">Dorrin Yard And Building Professional lawn care, landscaping, and property improvement in Northeast Arkansas.</p>
    <ul class="services">
      <li>Lawn maintenance</li>
      <li>Lawn treatments and weed control</li>
      <li>Exterior projects</li>
      <li>Custom landscape design &amp; installation</li>
      <li>Sod, trees, rock &amp; drainage solutions</li>
      <li>Residential &amp; commercial services Reliable</li>
    </ul>
    <div class="brand brand-front">
      <span class="brand-dot"></span>
      <span class="brand-name">Dorrin Yard &amp; Building LLC</span>
    </div>
  </section>

  <section class="card card-back">
    <div class="brand brand-back">
      <span class="brand-dot"></span>
      <span class="brand-name">Dorrin Yard<br>&amp; Building LLC</span>
    </div>
  </section>
</body>
</html>
```